Aerial photo/video drone company needs new business card

Aerial visual company who offers photos and video services via drones.

We are KTO certified and work in the real estate, insurance, construction, and film industries.

I'm looking for a clean, professional, maybe even edgy design, that will be a conversation starter when networking.

I've included our logo, current business card, and font.

Our current business card is decent; albeit, I'm looking for something more unique. If you folks provide good designs, I'll definitely guarantee payment (and I'm not opposed to tipping if the design is above and beyond).

Target Market(s)

Insurance companies, real estate agents, construction companies, advertising & other creative agencies, and filmmakers/producers.

Industry/Entity Type

Business

Contact Information for Business Card

Company name pronounced tol-u-mo.

Other font styles liked:
• Font was uploaded; that or similar; not opposed to other fonts if they work well with the design

Requirements
Must have
• Clearly prominent logo; my name and title; phone number; email address; web address; mentioned "KTO Certified" or similar; should indicate "Aerial visual"
Nice to have
• Watermark of logo or otherwise
Should not have
• Pictures of drones or scenic shots

```html
<!DOCTYPE html>
<html lang="en">
<head>
<meta charset="utf-8">
<title>tolumo — business card</title>
<link href="https://fonts.googleapis.com/css2?family=Montserrat:wght@500;600;700&display=swap" rel="stylesheet">
<style>
  :root {
    --backdrop: #2a2a2a;
    --navy: #233a5e;
    --blue: #2693d3;
    --white: #ffffff;
    --mist: #e4e4e4;
    --ink: #233a5e;
  }
  * { box-sizing: border-box; margin: 0; padding: 0; }
  html, body { width: 1200px; height: 852px; overflow: hidden; }
  body {
    background: var(--backdrop);
    font-family: "Montserrat", Arial, sans-serif;
    position: relative;
  }
  .card {
    position: absolute;
    top: 271px;
    width: 540px;
    height: 310px;
    border-radius: 22px;
    overflow: hidden;
  }

  /* Front */
  .card-front { left: 40px; background: var(--white); }
  .front-watermark {
    position: absolute; right: 30px; top: -40px;
    width: 230px; height: 230px; border-radius: 50%;
    background: var(--mist);
  }
  .front-logo {
    position: absolute; left: 0; right: 0; top: 92px;
    display: flex; align-items: center; justify-content: center; gap: 14px;
  }
  .logo-dot { width: 34px; height: 34px; border-radius: 50%; background: var(--navy); }
  .logo-name { font-weight: 700; font-size: 62px; color: var(--navy); letter-spacing: 1px; line-height: 1; }
  .services {
    position: absolute; left: 0; right: 0; top: 208px;
    text-align: center; font-weight: 700; font-size: 12.5px;
    color: var(--ink); letter-spacing: 0.4px;
  }
  .services .sep {
    display: inline-block; width: 8px; height: 8px; border-radius: 50%;
    background: var(--blue); margin: 0 5px; vertical-align: 1px;
  }
  .cert-band {
    position: absolute; left: 0; right: 0; bottom: 0; height: 56px;
    background: var(--blue); color: var(--white);
    display: flex; align-items: center; justify-content: center;
    font-weight: 600; font-size: 14px; letter-spacing: 1px;
  }

  /* Back */
  .card-back { left: 620px; background: var(--navy); color: var(--white); }
  .back-mark {
    position: absolute; right: -40px; top: 30px;
    width: 270px; height: 270px; border-radius: 50%;
    background: var(--blue);
  }
  .back-name {
    position: absolute; left: 36px; top: 58px;
    font-weight: 700; font-size: 58px; line-height: 1; color: var(--white); letter-spacing: 1px;
  }
  .person { position: absolute; left: 40px; top: 140px; }
  .person-name { font-weight: 700; font-size: 19px; letter-spacing: 0.5px; }
  .person-title { font-weight: 600; font-size: 14px; color: var(--blue); margin-top: 2px; }
  .address { margin-top: 12px; font-size: 12.5px; font-weight: 500; line-height: 1.4; }
  .contacts { list-style: none; margin-top: 8px; font-size: 12.5px; font-weight: 500; }
  .contacts li { display: flex; align-items: center; gap: 8px; line-height: 1.45; }
  .contacts svg { width: 11px; height: 11px; flex: none; }
</style>
</head>
<body>
  <section class="card card-front">
    <div class="front-watermark"></div>
    <div class="front-logo">
      <span class="logo-dot"></span>
      <span class="logo-name">tolumo</span>
    </div>
    <p class="services">ARIAL VISUAL FOR REAL ESTATE<span class="sep"></span>INSURANCE<span class="sep"></span>CONSTRUCTION<span class="sep"></span>FILM</p>
    <div class="cert-band">KTO PART 107 COMMERCIAL SUAS CERTIFIED</div>
  </section>

  <section class="card card-back">
    <div class="back-mark"></div>
    <div class="back-name">tolumo</div>
    <div class="person">
      <p class="person-name">MARCUS HALE</p>
      <p class="person-title">Managing Director</p>
      <p class="address">2217 Harbor Lane Suite 300<br>Fenwick, Il 60231</p>
      <ul class="contacts">
        <li><svg viewBox="0 0 12 12"><rect x="1" y="2" width="10" height="7" rx="1" fill="none" stroke="#2693d3" stroke-width="1.4"/><rect x="4" y="10" width="4" height="1.4" fill="#2693d3"/></svg>0481-226-907</li>
        <li><svg viewBox="0 0 12 12"><path d="M2 1.5 L4.5 1.5 L5.5 4 L4 5 Q5 7.5 7 8 L8 6.5 L10.5 7.5 L10.5 10 Q5 11 1.5 4 Z" fill="#2693d3"/></svg>0755-412-390</li>
        <li><svg viewBox="0 0 12 12"><rect x="1" y="2.5" width="10" height="7" fill="#2693d3"/><path d="M1 2.5 L6 7 L11 2.5" fill="none" stroke="#233a5e" stroke-width="1"/></svg>marcus@tolumo.com</li>
        <li><svg viewBox="0 0 12 12"><circle cx="6" cy="6" r="5" fill="none" stroke="#2693d3" stroke-width="1.2"/><ellipse cx="6" cy="6" rx="2" ry="5" fill="none" stroke="#2693d3" stroke-width="1"/><line x1="1" y1="6" x2="11" y2="6" stroke="#2693d3" stroke-width="1"/></svg>tolumoaerial.com</li>
      </ul>
    </div>
  </section>
</body>
</html>
```